Visitenkarten für Containerhandel
BROV
alles tip top wie bestellt so wurde geliefert!
Zielgruppe
Wir handeln mit See und Lagercontainer
Aufgabenstellung
evtl. Das Seecontainer Designe integrieren
Angaben auf der Karte;
//Frimenangaben//
TORVELMARK AG
Ribelweg 27
CH - 6237 Ledringen
sales@torvelmark.ch
//Personenangaben//
Lukas Brenni
Leiter Verkauf

```html
<!DOCTYPE html>
<html lang="de">
<head>
<meta charset="utf-8">
<title>TORVELMARK AG – Visitenkarten</title>
<link href="https://fonts.googleapis.com/css2?family=Arimo:ital,wght@0,400;0,700;1,400&display=swap" rel="stylesheet">
<style>
  :root {
    --bg: #e9ecec;
    --white: #ffffff;
    --black: #222222;
    --grey: #444444;
    --green: #3a9f4a;
    --green-light: #4fb866;
    --text: #1c1c1c;
  }
  * { margin: 0; padding: 0; box-sizing: border-box; }
  html, body { width: 1200px; height: 900px; overflow: hidden; background: var(--bg); }
  body { font-family: "Arimo", Arial, sans-serif; color: var(--text); }
  .canvas { position: relative; width: 1200px; height: 900px; }
  .card {
    position: absolute; left: 280px; width: 640px; height: 370px;
    background: var(--white); overflow: hidden;
    box-shadow: 0 10px 30px rgba(0,0,0,.12);
  }
  .card--front { top: 60px; }
  .card--back { top: 470px; }
  .card svg.stripes { position: absolute; inset: 0; }

  .wordmark {
    font-weight: 700; color: var(--text); letter-spacing: .04em; line-height: 1;
  }
  .card--front .wordmark {
    position: absolute; left: 0; right: 0; top: 160px; text-align: center; font-size: 50px;
  }

  .company { position: absolute; left: 44px; top: 100px; }
  .company .wordmark { font-size: 32px; margin-bottom: 26px; }
  .address { font-size: 15px; line-height: 1.35; }

  .contact { position: absolute; left: 380px; right: 0; top: 0; bottom: 0; color: var(--white); }
  .person { position: absolute; left: 34px; top: 48px; }
  .person-name { font-weight: 700; font-size: 24px; text-transform: uppercase; letter-spacing: .02em; }
  .person-role { font-style: italic; font-size: 22px; color: var(--green-light); margin-top: 4px; }
  .contact-line { position: absolute; left: 34px; display: flex; align-items: center; gap: 12px; font-size: 16px; }
  .contact-line svg { flex: none; }
  .contact-line--mail { top: 173px; }
  .contact-line--phone { top: 262px; }
</style>
</head>
<body>
<main class="canvas">

  <section class="card card--front" aria-label="Vorderseite">
    <svg class="stripes" width="640" height="370" viewBox="0 0 640 370" aria-hidden="true">
      <polygon points="0,0 50,0 50,130 70,150 70,220 50,240 50,370 0,370" fill="var(--black)"/>
      <polygon points="50,130 70,150 70,220 50,240 0,240 0,130" fill="var(--grey)"/>
      <polygon points="50,0 90,0 90,130 110,150 110,220 90,240 90,370 50,370 50,240 70,220 70,150 50,130" fill="var(--green)"/>
      <polygon points="640,0 590,0 590,130 570,150 570,220 590,240 590,370 640,370" fill="var(--black)"/>
      <polygon points="590,130 570,150 570,220 590,240 640,240 640,130" fill="var(--grey)"/>
      <polygon points="590,0 550,0 550,130 530,150 530,220 550,240 550,370 590,370 590,240 570,220 570,150 590,130" fill="var(--green)"/>
    </svg>
    <div class="wordmark">TORVELMARK</div>
  </section>

  <section class="card card--back" aria-label="Rückseite">
    <svg class="stripes" width="640" height="370" viewBox="0 0 640 370" aria-hidden="true">
      <polygon points="380,0 640,0 640,370 380,370 380,240 400,220 400,150 380,130" fill="var(--black)"/>
      <polygon points="390,140 640,140 640,230 390,230 400,220 400,150" fill="var(--grey)"/>
      <polygon points="340,0 380,0 380,130 400,150 400,220 380,240 380,370 340,370 340,240 360,220 360,150 340,130" fill="var(--green)"/>
    </svg>

    <div class="company">
      <div class="wordmark">TORVELMARK</div>
      <p class="address">TORVELMARK AG<br>Ribelweg 27<br>CH - 6237 Ledringen</p>
    </div>

    <div class="contact">
      <div class="person">
        <p class="person-name">Lukas Brenni</p>
        <p class="person-role">Leiter Verkauf</p>
      </div>
      <p class="contact-line contact-line--mail">
        <svg width="22" height="16" viewBox="0 0 22 16" aria-hidden="true">
          <rect x="1" y="1" width="20" height="14" fill="none" stroke="var(--green-light)" stroke-width="1.5"/>
          <polyline points="1,1 11,9 21,1" fill="none" stroke="var(--green-light)" stroke-width="1.5"/>
        </svg>
        sales@torvelmark.ch
      </p>
      <p class="contact-line contact-line--phone">
        <svg width="20" height="20" viewBox="0 0 24 24" aria-hidden="true">
          <path d="M6.6 10.8a15 15 0 0 0 6.6 6.6l2.2-2.2a1 1 0 0 1 1-.25 11.4 11.4 0 0 0 3.6.57 1 1 0 0 1 1 1V20a1 1 0 0 1-1 1A17 17 0 0 1 3 4a1 1 0 0 1 1-1h3.5a1 1 0 0 1 1 1c0 1.25.2 2.450.57 3.57a1 1 0 0 1-.25 1z" fill="none" stroke="var(--green-light)" stroke-width="1.6"/>
        </svg>
        +41 58 306 42 18
      </p>
    </div>
  </section>

</main>
</body>
</html>
```